Web design for consulting advisory business company

We need a web for our business consulting company. The web should transmit simplicity, innovation, trust, and solid knowledge of what we do. Inspirational webs to take a look are: https://brimlotte.com/ and http://varunexa.com.br. Use blue colors.

Target Market(s)

Private companies

Industry/Entity Type

Management Consulting

Number of Pages Required

5+ page

Font styles to use
Serif
Sans Serif

Colors
3176b5
3276b5
85abd2
85cae6
33a6d7
0592cd
ffffff
1b1b1b
474747

Requirements
Must have
• - use of blue
• - images
• - same version in different languages (portugueses and spanish)
Nice to have
• - white as background

```html
<!DOCTYPE html>
<html lang="en">
<head>
<meta charset="utf-8">
<title>Veltra Partners — Management Consulting</title>
<link href="https://fonts.googleapis.com/css2?family=Montserrat:wght@400;500;600;700&family=Open+Sans:wght@400;600&display=swap" rel="stylesheet">
<style>
:root{
  --blue:#3176b5;
  --blue-soft:#85abd2;
  --sky:#85cae6;
  --cyan:#33a6d7;
  --azure:#0592cd;
  --navy:#2a5f96;
  --white:#ffffff;
  --ink:#1b1b1b;
  --grey:#474747;
  --mist:#c9d7e8;
}
*{box-sizing:border-box;margin:0;padding:0}
html,body{width:1200px;height:4836px;overflow:hidden}
body{font-family:'Open Sans',Arial,sans-serif;color:var(--grey);background:var(--white);position:relative}
h1,h2,h3,.nav,.btn{font-family:'Montserrat',Arial,sans-serif}
.section{position:absolute;left:0;width:1200px}
.title{font-size:30px;font-weight:700;color:var(--blue);text-align:center;letter-spacing:.5px}
.lead{width:900px;margin:14px auto 0;text-align:center;font-size:12px;line-height:18px}
.btn{display:block;width:92px;height:34px;margin:0 auto;background:var(--ink);color:var(--white);font-size:12px;line-height:34px;text-align:center}

/* header */
.header{top:0;height:112px;display:flex;align-items:center;padding:0 140px}
.brand{display:flex;align-items:center;gap:10px;font-family:'Montserrat',sans-serif;font-weight:700;font-size:22px;color:var(--blue);letter-spacing:1px}
.brand .mark{width:30px;height:30px;background:var(--blue)}
.nav{display:flex;gap:26px;margin-left:auto;font-size:14px;color:var(--grey)}
.nav .active{color:var(--azure)}
.langs{display:flex;gap:6px;margin-left:20px}
.langs span{width:18px;height:12px;display:block}

/* hero */
.hero{top:112px;height:500px;background:linear-gradient(120deg,#5c6b7c,#8a96a4 45%,#4a5868);}
.hero::after{content:"";position:absolute;inset:0;background:rgba(20,30,45,.35)}
.hero h1{position:absolute;z-index:1;top:200px;width:100%;text-align:center;color:var(--white);font-size:30px;font-weight:700;line-height:38px}
.arrow{position:absolute;z-index:1;top:235px;width:34px;height:34px;background:var(--blue);display:flex;align-items:center;justify-content:center}

/* principles */
.principles{top:612px;height:528px;padding-top:80px}
.cards3{display:flex;gap:30px;width:870px;margin:34px auto 40px}
.pcard{flex:1;height:180px;color:var(--white);display:flex;flex-direction:column;align-items:center;justify-content:center;gap:22px;font-size:14px;font-family:'Montserrat',sans-serif}
.pcard:nth-child(1){background:var(--cyan)}
.pcard:nth-child(2){background:#2f96d6}
.pcard:nth-child(3){background:var(--blue)}

/* expertise */
.expertise{top:1140px;height:240px;background:#7fa3d0;padding-top:70px}
.expertise .title,.expertise .lead{color:var(--white)}
.split{top:1380px;height:640px;display:flex}
.split .col{flex:1;padding:82px 140px 0 140px;color:var(--white)}
.split .sectors{background:linear-gradient(135deg,#24568c,#2f6aa6)}
.split .services{background:linear-gradient(135deg,#3e82c4,#4b8dcb);text-align:right}
.split h2{font-size:28px;font-weight:700;margin-bottom:30px}
.split li{list-style:none;font-size:14px;line-height:30px}

/* cases */
.cases{top:2020px;height:720px;padding-top:70px}
.case-row{display:flex;gap:24px;width:904px;margin:30px auto 36px}
.case{flex:1}
.case .photo{height:220px}
.case .body{background:var(--blue);color:var(--white);height:196px;padding:26px 24px;font-size:12px;line-height:18px}
.case .more{display:inline-block;margin-top:18px;border:1px solid var(--white);padding:5px 14px;font-size:11px}

/* ecosystem */
.ecosystem{top:2740px;height:700px;background:#86a8d4;padding-top:64px}
.ecosystem .title,.ecosystem .lead{color:var(--white)}
.eco-grid{position:relative;width:904px;height:420px;margin:34px auto 0}
.eco{position:absolute;background:var(--white);display:flex;flex-direction:column;align-items:center;justify-content:center;text-align:center;gap:12px;font-size:13px;color:var(--grey);padding:0 20px}
.eco .name{font-family:'Montserrat',sans-serif;font-weight:700;font-size:24px;color:var(--ink)}
.eco .big{font-size:44px}

/* team */
.team{top:3440px;height:572px;padding-top:64px}
.members{display:flex;justify-content:center;gap:160px;margin-top:40px}
.member{text-align:center;width:180px}
.member .diamond{width:130px;height:130px;margin:25px auto 40px;transform:rotate(45deg);background:linear-gradient(135deg,#d9dde2,#9aa4b0)}
.member h3{font-size:15px;font-weight:600;color:var(--ink)}
.member p{font-size:12px;margin-top:4px}
.chev{position:absolute;top:220px}

/* contact */
.contact{top:4012px;height:468px;background:#3093d4;color:var(--white);padding-top:44px;text-align:center}
.contact .title{color:var(--white)}
.contact .tag{font-family:'Montserrat',sans-serif;font-size:20px;font-weight:600;margin-top:6px}
.contact .small{font-size:12px;line-height:18px;width:900px;margin:10px auto 0}
.contact .mail{font-size:14px;margin-top:10px}
.form{width:904px;margin:24px auto 0}
.fields{display:flex;gap:14px}
.field{flex:1;height:30px;background:var(--white);color:#9aa;font-size:11px;text-align:left;padding:8px 10px}
.msg{height:110px;margin-top:12px}
.form .btn{margin-top:20px}

/* offices */
.offices{top:4480px;height:260px;padding-top:52px;background:#fafbfd}
.offices .title{color:var(--mist)}
.office-row{display:flex;width:904px;margin:34px auto 0;justify-content:space-between}
.office{width:280px;font-size:12px;line-height:18px}
.office h3{font-size:13px;color:var(--blue);font-weight:700;margin-bottom:4px}

/* footer */
.footer{top:4740px;height:96px;background:var(--ink);color:#bbb;font-size:11px;padding:24px 140px}
.footer .links{display:flex;gap:18px}
.footer .copy{margin-top:10px;color:#888}
.footer .social{position:absolute;right:140px;top:30px;display:flex;gap:12px}
.footer .social span{width:14px;height:14px;border-radius:50%;background:#bbb;display:block}
</style>
</head>
<body>

<header class="section header">
  <div class="brand"><span class="mark"></span>VELTRA PARTNERS</div>
  <nav class="nav">
    <span class="active">Principles</span><span>Expertise</span><span>Cases</span><span>Ecosystem</span><span>Team</span><span>Contact us</span>
  </nav>
  <div class="langs"><span style="background:#c0392b"></span><span style="background:#2c5aa0"></span></div>
</header>

<section class="section hero" role="img" aria-label="Team of consultants planning around a table covered with sticky notes and charts">
  <h1>VESTIBULUM CONDIMENTUM RISUS POSUERE<br>VELIT JUSTO ACCUMSAN</h1>
  <div class="arrow" style="left:48px"><svg width="12" height="14"><path d="M9 1L3 7l6 6" stroke="#fff" stroke-width="2" fill="none"/></svg></div>
  <div class="arrow" style="right:48px"><svg width="12" height="14"><path d="M3 1l6 6-6 6" stroke="#fff" stroke-width="2" fill="none"/></svg></div>
</section>

<section class="section principles">
  <h2 class="title">PRINCIPLES</h2>
  <p class="lead">We take the team and efforts to the problem by combining senior resources and industry experts with strong analytical resources to deliver sustainable solutions. We listen carefully to our customers and combine our teams with your needs. If the project scope changes we change the configuration. We think of implementation from day one and allow the leaders with whom we work to mobilize their people.</p>
  <div class="cards3">
    <div class="pcard">
      <svg width="56" height="56" viewBox="0 0 56 56" fill="none" stroke="#fff" stroke-width="2.5"><rect x="6" y="24" width="10" height="26"/><path d="M16 26l10-18c4 0 6 3 5 7l-2 8h15c3 0 5 3 4 6l-4 16c-1 3-3 5-6 5H16"/></svg>
      Flexibility
    </div>
    <div class="pcard">
      <svg width="64" height="56" viewBox="0 0 64 56" fill="none" stroke="#fff" stroke-width="2.5"><path d="M2 18l12-6 10 4M62 18l-12-6-14 6-10 8c2 3 6 3 8 1l6-4 14 12"/><path d="M14 12v22l14 14c2 2 5 0 4-2M24 40l8 8c2 2 5 0 4-2M30 36l8 8c2 2 5 0 4-2M50 12v22"/></svg>
      Co-creation with the client
    </div>
    <div class="pcard">
      <svg width="56" height="56" viewBox="0 0 56 56" fill="none" stroke="#fff" stroke-width="2.5"><path d="M4 52h48"/><rect x="8" y="36" width="8" height="16"/><rect x="22" y="28" width="8" height="24"/><rect x="36" y="18" width="8" height="34"/><path d="M8 26L30 10l6 4 14-10M42 4h8v8"/></svg>
      Sustainable results
    </div>
  </div>
  <a class="btn">View All</a>
</section>

<section class="section expertise">
  <h2 class="title">EXPERTISE</h2>
  <p class="lead">A mix of senior advisors, combined with industry experts, ensures sustainable results for our customers. We adapt the team and effort to each client, and we create impact through insight and guidance in practice. When necessary we join experts and partners from every corner of the world.</p>
</section>

<section class="section split">
  <div class="col sectors">
    <h2>SECTORS</h2>
    <ul><li>Consumer Goods</li><li>Retail</li><li>Financial Services</li><li>Health</li><li>Tel Co &amp; Media</li><li>Sports and Major Events</li><li>Transportation &amp; Logistics</li><li>Energy &amp; Environment</li><li>Private Equity</li></ul>
  </div>
  <div class="col services">
    <h2>SERVICES</h2>
    <ul><li>Strategic Planning</li><li>Commercial</li><li>Operations</li><li>People &amp; Organization</li><li>Data Analytics</li><li>Innovation</li><li>Digital</li><li>Transformation</li><li>Circular Economy</li><li>PMO &amp; Change Management</li><li>Training</li></ul>
  </div>
</section>

<section class="section cases">
  <h2 class="title">CASES</h2>
  <p class="lead">Our senior team has extensive experience in high impact projects. Some of these experiences include:</p>
  <div class="case-row">
    <div class="case">
      <div class="photo" role="img" aria-label="Consultants reviewing documents at a meeting table" style="background:linear-gradient(135deg,#b9c6d3,#6f8296)"></div>
      <div class="body">Identification of the main synergies, preparation of the business model and the integration plan of two major Brazilian financial institutions; restructuring and monitoring of the implementation of the Project Management Office (PMO).<br><span class="more">Read More</span></div>
    </div>
    <div class="case">
      <div class="photo" role="img" aria-label="Hands working on a laptop with printed charts" style="background:linear-gradient(135deg,#d6dee6,#8798aa)"></div>
      <div class="body">Development of annual budget and three-year investment plan for a large Brazilian Financial Services Company, identifying options to improve the efficiency of total budget.<br><span class="more">Read More</span></div>
    </div>
  </div>
  <a class="btn">View All</a>
</section>

<section class="section ecosystem">
  <h2 class="title">ECOSYSTEM</h2>
  <p class="lead">We are global experts and partners from around the world. The need for speed and complexity of problems requires a flexible approach, and an ecosystem offers access to worldwide knowledge of world-class industry leaders.</p>
  <div class="eco-grid">
    <div class="eco" style="left:0;top:0;width:288px;height:196px"><span class="name">Norvik Group</span>Global network of over 900,000 independent experts from various industries</div>
    <div class="eco" style="left:0;top:214px;width:288px;height:196px"><span class="name">PanelHive</span>Global network of behavioral experts</div>
    <div class="eco" style="left:308px;top:0;width:288px;height:410px"><span class="name big">Quanta.AI</span>Artificial intelligence platform and service</div>
    <div class="eco" style="left:616px;top:0;width:288px;height:196px"><span class="name">Lyceum</span>Research institute</div>
    <div class="eco" style="left:616px;top:214px;width:288px;height:196px"><span class="name">Brightpulse</span>End to end solution for Internet of Things innovations</div>
  </div>
</section>

<section class="section team">
  <h2 class="title">SENIOR TEAM</h2>
  <svg class="chev" style="left:70px" width="14" height="24"><path d="M12 2L3 12l9 10" stroke="#999" stroke-width="2" fill="none"/></svg>
  <svg class="chev" style="right:70px" width="14" height="24"><path d="M2 2l9 10-9 10" stroke="#999" stroke-width="2" fill="none"/></svg>
  <div class="members">
    <div class="member"><div class="diamond" role="img" aria-label="Portrait of a senior partner"></div><h3>Tomás Verrant</h3><p>Aliquam erat volutpat</p></div>
    <div class="member"><div class="diamond" role="img" aria-label="Portrait of a senior partner"></div><h3>Rafael Ostrand</h3><p>Fusce sollicitudin</p></div>
  </div>
</section>

<section class="section contact">
  <h2 class="title">CONTACT</h2>
  <p class="tag">Advance with confidence.</p>
  <p class="small">Contact us for more information on how Veltra Partners can help you achieve greater results, optimize performance and improve your business growth.</p>
  <p class="mail">Use the contact form below or send us an email directly to<br>contact@veltra-partners.com.br</p>
  <div class="form">
    <div class="fields"><div class="field">Name</div><div class="field">Organization</div><div class="field">Telephone</div><div class="field">Email</div></div>
    <div class="field msg">Message</div>
    <a class="btn">Submit</a>
  </div>
</section>

<section class="section offices">
  <h2 class="title">CONTACT INFORMATION</h2>
  <div class="office-row">
    <div class="office"><h3>RIO DE JANEIRO</h3>Rua das Palmeiras, 88 - 6º andar - Centro<br>Rio de Janeiro | 20011-300 | RJ</div>
    <div class="office"><h3>SÃO PAULO</h3>Rua Jacarandá, 415 - Sala 32 - Itaim<br>São Paulo | 04532-110 | SP</div>
    <div class="office"><h3>BUENOS AIRES</h3>Calle Los Álamos 2250 - Piso 3<br>Buenos Aires | C1425 | Argentina</div>
  </div>
</section>

<footer class="section footer">
  <div class="links"><span>Principles</span><span>Expertise</span><span>Cases</span><span>Ecosystem</span><span>Team</span><span>Contact us</span></div>
  <p class="copy">Copyright © 2019 - Veltra Partners. All Rights Reserved.</p>
  <div class="social"><span></span><span></span></div>
</footer>

</body>
</html>
```